BasinVerde Wordpress Design Project

BasinVerde is a retrofit for your toilet lid that turns it into a sink. By rerouting clean water from the supply line, BasinVerde delivers an automatic, touch-free hand wash with every flush. We already have a wordpress site, but would like to create a "fresh face" for our company, emphasizing the green aspect of our product. Therefore, we want to include both blue and green colors in the design. you can look at our current website here: www.basinverde-example.com. Our old website seems dated and disorganized, we want our new website to be brighter and more inviting.

Target Market(s)

green homeowners, those interested in saving money and resources

Industry/Entity Type

It Company

Requirements
Nice to have
• We want to emphasize the simplicity of our product, and feel that our website should represent that. We would like to have a place for videos, social media links, as well as a menu that has about us/Frequently asked questions/store/etc.

```html
<!DOCTYPE html>
<html lang="en">
<head>
<meta charset="utf-8">
<title>BasinVerde – The Patented Multi-Purpose Accessory Sink</title>
<link href="https://fonts.googleapis.com/css2?family=Jura:wght@500;600;700&family=PT+Sans+Narrow:wght@400;700&family=Noto+Sans:wght@400;700&display=swap" rel="stylesheet">
<style>
:root{
  --page-top:#ffffff;
  --page-bottom:#7ffcfc;
  --brand-blue:#1f86c8;
  --nav-top:#4ab3f3;
  --nav-bottom:#0b5fb8;
  --leaf:#6b9f2c;
  --panel-cyan:#5ffcfc;
  --frame-blue:#2a8de0;
  --ink:#1a1a1a;
  --link:#1a55c9;
  --white:#ffffff;
}
*{margin:0;padding:0;box-sizing:border-box}
html,body{width:1200px;height:900px;overflow:hidden}
body{
  position:relative;
  background:linear-gradient(180deg,var(--page-top) 0,var(--page-top) 90px,var(--page-bottom) 600px,var(--page-bottom) 100%);
  font-family:"PT Sans Narrow",sans-serif;color:var(--ink);
}
.abs{position:absolute}
.top-rule{left:0;top:0;width:1200px;height:4px;background:var(--leaf)}

/* header */
.brand{left:124px;top:6px}
.brand-name{font-family:"Jura",sans-serif;font-weight:600;font-size:58px;color:var(--brand-blue);letter-spacing:-1px;line-height:64px;white-space:nowrap}
.brand-tagline{font-family:"Jura",sans-serif;font-weight:600;font-size:15px;color:var(--brand-blue);margin-left:16px;margin-top:3px;white-space:nowrap}
.search{left:880px;top:38px;width:209px;height:29px;border:1px solid var(--frame-blue);background:var(--white);display:flex;align-items:center;padding:0 4px;gap:5px;font-family:"Noto Sans",sans-serif;font-size:9px;font-weight:700;color:#555}
.search-field{width:122px;height:19px;border:1px solid #888;box-shadow:inset 1px 1px 2px #aaa}
.search-go{display:flex;align-items:center;gap:4px}

/* navigation */
.main-nav{left:120px;top:95px;width:969px;height:42px;background:linear-gradient(180deg,var(--nav-top),var(--nav-bottom));border:1px solid var(--frame-blue)}
.main-nav a{position:absolute;top:11px;font-family:"Jura",sans-serif;font-weight:600;font-size:14px;color:var(--white);text-decoration:none;letter-spacing:.2px;white-space:nowrap}

/* hero */
.hero-photo{left:121px;top:137px;width:596px;height:398px;border:1px solid var(--frame-blue);
  background:radial-gradient(ellipse at 55% 70%,#fff1dc 0,#e9cfa6 35%,#a88a5a 65%,#6e5a30 100%)}
.feature-lead{left:717px;top:137px;width:372px;height:82px;background:var(--leaf);color:var(--white);padding:10px 11px}
.feature-lead::before{content:"";position:absolute;left:-20px;top:26px;border:12px solid transparent;border-right:10px solid var(--leaf)}
.feature-lead h2{font-size:22px;font-weight:700;margin-bottom:7px}
.feature-lead p{font-size:14px}
.feature-item{left:717px;width:372px;height:78px;background:var(--panel-cyan);border-bottom:2px solid #4a7a86;font-size:12.5px;line-height:17px;padding:33px 10px 0;white-space:nowrap;overflow:hidden;letter-spacing:-.15px}

/* lower columns */
.col-head{top:549px;height:35px;background:var(--leaf);border:2px solid var(--frame-blue);display:flex;align-items:center;justify-content:space-between;padding:0 12px;color:var(--link);font-size:19px;font-weight:400;white-space:nowrap}
.col-head svg{flex:none}
.headline-list{left:125px;top:587px;width:215px;font-family:"Noto Sans",sans-serif;font-size:10.5px;line-height:14.5px}
.headline-list time{display:block;font-weight:700;font-size:11.5px;margin-bottom:5px}
.headline-list li{list-style:none;margin-bottom:16px}
.scroll-track{left:342px;top:589px;width:9px;height:190px;background:#5a8a92;border-radius:5px}
.scroll-thumb{left:345px;top:597px;width:3px;height:75px;background:#2d5560}
.more-link{font-size:14px;color:var(--link);text-decoration:underline;white-space:nowrap}
.buy-copy{left:380px;top:592px;width:215px;font-size:15px;line-height:18px}
.buy-copy p{margin-bottom:12px}
.video-frame{left:639px;top:595px;width:189px;height:178px;background:#111;border:1px solid #333}
.video-still{left:0;top:0;width:187px;height:152px;background:radial-gradient(ellipse at 55% 45%,#f2f2f2 0,#b9b9b9 45%,#3a3a3a 100%)}
.video-bar{left:0;top:152px;width:187px;height:24px;background:#1c1c1c;display:flex;align-items:center;padding:0 4px;gap:6px}
.video-play{width:15px;height:14px;background:#1a9ad6;display:flex;align-items:center;justify-content:center}
.video-track{width:92px;height:3px;background:#555;position:relative}
.video-track span{position:absolute;left:0;top:0;width:42px;height:3px;background:#1a9ad6}
.studio-copy{left:857px;top:587px;width:228px;font-size:14.5px;line-height:19px;text-align:justify;letter-spacing:-.2px}

/* footer */
.site-footer{left:0;top:790px;width:1200px;height:110px;background:repeating-linear-gradient(45deg,#5d8e30 0 2px,#55852a 2px 4px);color:var(--white)}
.foot-title{font-family:"Jura",sans-serif;font-weight:600;font-size:12.5px;letter-spacing:.5px;white-space:nowrap}
.quick-nav{display:grid;grid-template-columns:129px 90px;font-family:"Jura",sans-serif;font-weight:600;font-size:12.5px;line-height:14.5px}
.partner-badge{left:455px;top:32px;width:231px;height:63px;background:var(--white);display:flex;align-items:center;padding:0 8px;gap:10px}
.partner-badge span{display:block}
.social{display:flex;gap:13px}
.social span{width:26px;height:26px;border-radius:3px}
.copyright{font-size:13px;font-weight:700;white-space:nowrap}
</style>
</head>
<body>
<div class="abs top-rule"></div>

<header>
  <div class="abs brand">
    <div class="brand-name">BasinVerde</div>
    <div class="brand-tagline">The Patented Multi-Purpose Accessory Sink</div>
  </div>
  <form class="abs search">
    <span>SEARCH</span><span class="search-field"></span>
    <span class="search-go">GO <svg width="5" height="7"><path d="M0 0L5 3.5 0 7z" fill="#555"/></svg></span>
  </form>
</header>

<nav class="abs main-nav">
  <a style="left:53px">HOME</a><a style="left:118px">ABOUT US</a><a style="left:213px">BENEFITS</a><a style="left:305px">SPECS/FAQ</a><a style="left:409px">PARTNERS</a><a style="left:508px">RETAILERS</a><a style="left:608px">PROGRAM</a><a style="left:701px">STORE</a><a style="left:772px">NEWS</a><a style="left:840px">CONTACT</a>
</nav>

<section>
  <div class="abs hero-photo" role="img" aria-label="Photo of the accessory sink on a toilet tank with water flowing from a curved faucet"></div>
  <div class="abs feature-lead"><h2>Conserves Water</h2><p>Fresh water for your hands, grey water for the bowl.</p></div>
  <div class="abs feature-item" style="top:221px">Lorem Ipsum is simply dummy text of the printing and typesetting industry.<br>Lorem Ipsum has been the industry's standard dummy text ever since the 1500s,</div>
  <div class="abs feature-item" style="top:301px">Lorem Ipsum is simply dummy text of the printing and typesetting industry.<br>Lorem Ipsum has been the industry's standard dummy text ever since the 1500s,</div>
  <div class="abs feature-item" style="top:381px">Lorem Ipsum is simply dummy text of the printing and typesetting industry.<br>Lorem Ipsum has been the industry's standard dummy text ever since the 1500s,</div>
  <div class="abs feature-item" style="top:461px;height:75px;padding-top:29px">Lorem Ipsum is simply dummy text of the printing and typesetting industry.<br>Lorem Ipsum has been the industry's standard dummy text ever since the 1500s,</div>
</section>

<section>
  <h3 class="abs col-head" style="left:121px;width:236px">Recent Headlines <svg width="32" height="10"><path d="M0 5H29M24 1L30 5 24 9" stroke="#1a55c9" stroke-width="1.6" fill="none"/></svg></h3>
  <ul class="abs headline-list">
    <li><time>22.09.2012</time>Lorem Ipsum is simply dummy text of the printing and typesetting industry.</li>
    <li><time>18.09.2012</time>Lorem Ipsum is simply dummy text of the printing and typesetting industry.</li>
    <li><time>15.19.2012</time>Lorem Ipsum is simply dummy text of the printing and typesetting industry.</li>
  </ul>
  <div class="abs scroll-track"></div><div class="abs scroll-thumb"></div>
  <a class="abs more-link" style="left:276px;top:764px">view more</a>

  <h3 class="abs col-head" style="left:376px;width:236px">Where To Buy <svg width="32" height="10"><path d="M0 5H29M24 1L30 5 24 9" stroke="#1a55c9" stroke-width="1.6" fill="none"/></svg></h3>
  <div class="abs buy-copy">
    <p>Lorem Ipsum is simply dummy text of the printing and typesetting industry. Lorem Ipsum has been the industry's standard dummy text ever since the 1500s,</p>
    <p>Lorem Ipsum is simply dummy text of the printing and typesetting industry. Lorem Ipsum has been the industry's standard dummy text ever since the 1500s,</p>
  </div>
  <a class="abs more-link" style="left:505px;top:763px">Leafline Market</a>

  <h3 class="abs col-head" style="left:632px;width:203px">How It Works <svg width="32" height="10"><path d="M0 5H29M24 1L30 5 24 9" stroke="#1a55c9" stroke-width="1.6" fill="none"/></svg></h3>
  <div class="abs video-frame">
    <div class="abs video-still" role="img" aria-label="Video still of the white accessory sink with its chrome faucet"></div>
    <div class="abs video-bar"><span class="video-play"><svg width="6" height="7"><path d="M0 0L6 3.5 0 7z" fill="#fff"/></svg></span><span class="video-track"><span></span></span></div>
  </div>

  <h3 class="abs col-head" style="left:852px;width:237px">Evergreen Design Co.</h3>
  <p class="abs studio-copy">Lorem Ipsum is simply dummy text of the printing and typesetting industry. Lorem Ipsum has been the industry's standard dummy text ever since the 1500s, when an unknown printer took a galley of type and scrambled it to make a type specimen book. It has survived not only five centuries, but also the leap into electronic typesetting,</p>
  <a class="abs more-link" style="left:1034px;top:764px">read more</a>
</section>

<footer class="abs site-footer">
  <div class="abs foot-title" style="left:171px;top:9px">QUICK NAVIGATION</div>
  <div class="abs quick-nav" style="left:146px;top:30px">
    <span>HOME</span><span>RETAILERS</span><span>ABOUT US</span><span>PROGRAM</span><span>BENEFITS</span><span>STORE</span><span>SPECS/FAQ</span><span>NEWS</span><span>PARTNERS</span><span>CONTACT</span>
  </div>
  <div class="abs foot-title" style="left:502px;top:9px">STRATEGIC PARTNERS</div>
  <div class="abs partner-badge" role="img" aria-label="Strategic partner badge">
    <span style="width:170px;height:40px;background:#2f6f3a;border-radius:3px"></span>
    <span style="width:34px;height:52px;background:#8fbf3a"></span>
  </div>
  <div class="abs foot-title" style="left:872px;top:9px">YOU MAY FOLLOW US ON</div>
  <div class="abs social" style="left:876px;top:41px" aria-label="Social media links">
    <span style="background:#4fb8e6"></span><span style="background:#c23a2b"></span><span style="background:#2f5a9c"></span><span style="background:#1d7bb7"></span>
  </div>
  <div class="abs copyright" style="left:793px;top:86px">© 2009 - 2012 Evergreen Design Co. All rights reserved.</div>
</footer>

</body>
</html>
```